Harborlight Counsel Group Brochure / flyer

Hey friends, My company is a consulting company for churches and Christian leaders. www.harborlightcounselgroup.example - I am creating a sales brochure to be able to place in leaders hands as they are interested in potentially hiring us. I would also like to use whatever is created as a page on our website. I would like to see the design match the flavor and feel of our website (Target audience is leaders ages 25-35) No church images or churchy feel. The final design should communicate professionalism and youth. Attached is the logo, the content & copy as well as an example of a project I really like. Send me any questions you might have.

Target Market(s)

25-35 leaders

Industry/Entity Type

Leadership

Requirements
Must have
• Nice look and feel that flows and feels like our website - harborlightcounselgroup.example
Should not have
• Church images - any churchy feel

```html
<!DOCTYPE html>
<html lang="en">
<head>
<meta charset="utf-8">
<title>Harborlight Counsel Group – Flyer</title>
<link rel="stylesheet" href="https://fonts.googleapis.com/css2?family=Oswald:wght@300;400;600&family=Open+Sans:ital,wght@0,400;0,600;0,700;1,400&display=swap">
<style>
  :root {
    --coral: #d9695b;
    --coral-dark: #c4584b;
    --slate: #5b5757;
    --slate-dark: #4a4646;
    --paper: #efeeec;
    --ink: #3c3a3a;
    --white: #ffffff;
  }
  * { box-sizing: border-box; margin: 0; padding: 0; }
  html, body { width: 900px; height: 1200px; overflow: hidden; background: var(--white); }
  .flyer {
    position: relative; width: 900px; height: 1200px; overflow: hidden;
    background: linear-gradient(180deg, #f6f5f3 0%, var(--paper) 100%);
    font-family: "Open Sans", Arial, sans-serif; color: var(--ink);
  }
  .masthead {
    position: absolute; left: 0; top: 0; width: 900px; height: 200px;
    background: linear-gradient(180deg, #e07c6e 0%, var(--coral) 100%);
    text-align: center; color: var(--white);
  }
  .masthead__title {
    font-family: "Oswald", sans-serif; font-weight: 300; font-size: 74px;
    line-height: 1; padding-top: 34px; letter-spacing: 1px;
  }
  .masthead__tagline {
    font-family: "Oswald", sans-serif; font-weight: 400; font-size: 25px;
    letter-spacing: 2px; margin-top: 16px;
  }
  .hero-photo {
    position: absolute; left: 50px; top: 175px; width: 300px; height: 300px;
    border-radius: 50%; border: 10px solid var(--white);
    box-shadow: 0 0 0 6px var(--coral), 0 6px 14px rgba(0,0,0,.25);
    background: radial-gradient(circle at 40% 35%, #e9d8c2 0%, #a78b72 45%, #5b4a40 100%);
  }
  .mission {
    position: absolute; left: 390px; top: 245px; width: 470px; height: 180px;
    background: var(--slate); color: var(--white);
    padding: 34px 36px; box-shadow: 0 6px 14px rgba(0,0,0,.25);
  }
  .mission__title { font-weight: 700; font-size: 22px; letter-spacing: .5px; }
  .mission__text { font-size: 21px; line-height: 1.35; margin-top: 6px; }
  .pillars {
    position: absolute; left: 40px; top: 505px; width: 820px;
    display: grid; grid-template-columns: 190px 1fr 1fr 1fr; gap: 18px;
  }
  .pillar { font-size: 17px; line-height: 1.35; }
  .pillar__head { color: var(--coral); font-weight: 700; font-size: 22px; }
  .pillar__head--inline { font-size: 20px; }
  .pillar--model .pillar__list { font-size: 16px; margin-top: 6px; line-height: 1.45; }
  .testimonial {
    position: absolute; left: 40px; top: 710px; width: 820px; height: 320px;
    background: var(--slate); color: var(--white); z-index: 2;
    box-shadow: 0 8px 18px rgba(0,0,0,.3);
  }
  .testimonial__tab {
    position: absolute; left: 0; top: 0; width: 330px; height: 54px;
    background: var(--coral); color: var(--white);
    font-weight: 700; font-size: 24px; padding: 12px 22px;
  }
  .testimonial__author {
    position: absolute; left: 30px; top: 78px; font-weight: 700; font-size: 19px;
  }
  .testimonial__quote {
    position: absolute; left: 30px; top: 118px; width: 760px;
    font-style: italic; font-size: 15px; line-height: 1.5; color: #ecebea;
  }
  .city-photo {
    position: absolute; left: 0; top: 880px; width: 900px; height: 320px;
    background: linear-gradient(180deg, #b9b2ad 0%, #8c817c 50%, #6f6461 100%);
  }
  .city-photo__tint {
    position: absolute; inset: 0;
    background: linear-gradient(180deg, rgba(217,105,91,.15) 40%, rgba(217,105,91,.85) 100%);
  }
  .site-url {
    position: absolute; left: 0; bottom: 28px; width: 900px; text-align: center;
    font-family: "Oswald", sans-serif; font-weight: 400; font-size: 34px;
    color: var(--white); letter-spacing: 1px; z-index: 3;
  }
</style>
</head>
<body>
<main class="flyer">
  <header class="masthead">
    <h1 class="masthead__title">Harborlight Counsel Group</h1>
    <p class="masthead__tagline">CONNECTING GREAT LEADERS TO GREAT IDEAS</p>
  </header>

  <div class="hero-photo" role="img" aria-label="Photo of a busy city street with people walking"></div>

  <section class="mission">
    <h2 class="mission__title">OUR MISSION–</h2>
    <p class="mission__text">To Awaken Gods People, To Equip Gods Family and to Unleash Gods Mission.</p>
  </section>

  <section class="pillars">
    <div class="pillar pillar--model">
      <div class="pillar__head">OUR MODEL:</div>
      <div class="pillar__list">AWAKEN (Eph 5:14)<br>UNLEASH (Matt 28)<br>EQUIP (2Tim2:2)</div>
    </div>
    <p class="pillar"><span class="pillar__head pillar__head--inline">Awaken:</span> Moving from Consumer to Contributor (I have a role in the kingdom of God)</p>
    <p class="pillar"><span class="pillar__head pillar__head--inline">Equip:</span> Moving from a Follower to a Leader (Leaders develop other Leaders)</p>
    <p class="pillar"><span class="pillar__head pillar__head--inline">UNLEASH:</span> Moving from Purposeless to a Life of Purpose (I have a Mission)</p>
  </section>

  <div class="city-photo" role="img" aria-label="Photo of a city skyline seen from above">
    <div class="city-photo__tint"></div>
  </div>

  <section class="testimonial">
    <div class="testimonial__tab">Testimonial-</div>
    <p class="testimonial__author">Darren Holt ~ Sr Pastor ~ Cedar Ridge Church ~ Lakeview Ohio</p>
    <p class="testimonial__quote">“Harborlight Counsel Group provided a place for me to learn and process how to lead the church in mission and discipleship. It wasn't about trying to get me to fit into a mold or program but about growing into who God was calling me to be and what he wants me to do. Our church, in turn, has seen a lot of fruit from the coaching and training I have received from Harborlight Counsel Group because it has helped shift our culture into one of mission and discipleship.”</p>
  </section>

  <p class="site-url">www.harborlightcounselgroup.example</p>
</main>
</body>
</html>
```